I need a business card design for a new company that will be doing consulting work around issues of cultural competency, and diversity and inclusion. I would like the design to be crisp and clear with bold but conservative colors and incorporate shades of blue

Target Market(s)

Small businesses, schools, non-profits

Industry/Entity Type

Consulting

Font styles to use
Serif
Sans Serif

Colors
0c5ba6
6b449b
3276b5
0292cd

Requirements
Must have
• A Morrow Venture (name of company)
• Tiru Morrow
• CEO
• tiru@amorrowventure.example
• (215)555-0147

```html
<!DOCTYPE html>
<html lang="en">
<head>
<meta charset="utf-8">
<title>A Morrow Venture — Business Card</title>
<link rel="stylesheet" href="https://fonts.googleapis.com/css2?family=Cinzel:wght@600&family=Arimo:wght@400&display=swap">
<style>
  :root {
    --blue-deep: #0c5ba6;
    --blue-mid: #3276b5;
    --blue-bright: #0292cd;
    --ink: #333333;
    --paper: #ffffff;
    --backdrop: #eceef1;
  }
  * { margin: 0; padding: 0; box-sizing: border-box; }
  html, body {
    width: 1200px; height: 900px; overflow: hidden;
    background: var(--backdrop);
  }
  .stage { position: relative; width: 1200px; height: 900px; }

  .card {
    position: absolute;
    width: 520px; height: 297px;
    border-radius: 3px;
    box-shadow: 0 6px 18px rgba(0,0,0,0.18);
    overflow: hidden;
  }

  /* Front */
  .card-front {
    left: 80px; top: 140px;
    background: var(--blue-bright);
    display: flex; flex-direction: column; align-items: center; justify-content: center;
    gap: 18px;
  }
  .brand-dot {
    width: 64px; height: 64px; border-radius: 50%;
    border: 0; background: var(--paper);
  }
  .brand-name {
    font-family: 'Cinzel', serif; font-weight: 600;
    font-size: 34px; letter-spacing: 1px;
    color: var(--paper);
  }

  /* Back */
  .card-back {
    left: 600px; top: 470px;
    background: var(--paper);
  }
  .card-back .wave { position: absolute; left: 0; top: 0; width: 520px; height: 297px; }
  .holder { position: absolute; left: 52px; top: 64px; }
  .holder-name {
    font-family: 'Cinzel', serif; font-weight: 600;
    font-size: 19px; color: var(--blue-deep); letter-spacing: 0.5px;
  }
  .holder-role {
    font-family: 'Arimo', sans-serif; font-size: 15px; color: var(--ink);
    margin-top: 4px; margin-left: 8px;
  }
  .back-brand {
    position: absolute; right: 26px; top: 30px;
    display: flex; flex-direction: column; align-items: center; gap: 10px;
  }
  .back-brand .brand-dot { width: 50px; height: 50px; background: var(--blue-deep); }
  .back-brand .brand-name { font-size: 22px; color: var(--blue-deep); }

  .contact {
    position: absolute; left: 52px; top: 172px;
    list-style: none;
    font-family: 'Arimo', sans-serif; font-size: 14px; color: var(--ink);
  }
  .contact li { display: flex; align-items: center; gap: 7px; margin-bottom: 6px; }
  .contact svg { width: 13px; height: 13px; flex: none; }
</style>
</head>
<body>
<main class="stage">
  <section class="card card-front" aria-label="Card front">
    <span class="brand-dot"></span>
    <span class="brand-name">A Morrow Venture</span>
  </section>

  <section class="card card-back" aria-label="Card back">
    <svg class="wave" viewBox="0 0 520 297" aria-hidden="true">
      <path d="M0,297 L0,262 C170,262 330,225 470,150 C490,140 505,132 520,126 L520,297 Z" fill="#0292cd"/>
      <path d="M0,262 C170,262 330,225 470,150 C350,238 180,272 0,274 Z" fill="#0c5ba6"/>
      <path d="M0,274 C180,272 350,238 470,150 C360,248 190,282 0,283 Z" fill="#ffffff"/>
    </svg>

    <div class="holder">
      <div class="holder-name">Tiru Morrow</div>
      <div class="holder-role">CEO</div>
    </div>

    <div class="back-brand">
      <span class="brand-dot"></span>
      <span class="brand-name">A Morrow Venture</span>
    </div>

    <ul class="contact">
      <li>
        <svg viewBox="0 0 16 16" aria-hidden="true"><path fill="#0292cd" d="M3 1.5l3 .5 1 3-2 1.5a9 9 0 0 0 4.5 4.5L11 9l3 1 .5 3-2 1.5C7 14 2 9 1.5 3.5z"/></svg>
        (215)555-0147
      </li>
      <li>
        <svg viewBox="0 0 16 16" aria-hidden="true"><rect x="1" y="3" width="14" height="10" fill="#0292cd"/><path d="M1.5 3.5L8 9l6.5-5.5" stroke="#fff" stroke-width="1.3" fill="none"/></svg>
        tiru@amorrowventure.example
      </li>
    </ul>
  </section>
</main>
</body>
</html>
```